Local Directory Ad

We currently have an advertisement in our local directory (see attached). We would like to make it look more appealing.
Dimensions are 110mm H X 175mm W
We would like to keep the same colours and contact details remain the same.
Most of the content can remain the same, Just remove the line Tax effective remote area salary packaging and add in Self Managed Super Funds.We want to change mortgage broking to Mortgage Broking and Loan Structuring.

We want to change the line Local accountants Local Knowledge Local Experience - to something like local knowledge beyond compare or unsurpassed local knowledge but open to suggestions on this.

there are some good designs posted so far. I particulalry like the ones from pulmawick, korbu41, and the last one posted by wexlorunti and PLV. Keep up the good work guys

```html
<!DOCTYPE html>
<html lang="en">
<head>
<meta charset="utf-8">
<title>Ridgeway Accounting &amp; Finance – Directory Ad</title>
<link rel="stylesheet" href="https://fonts.googleapis.com/css2?family=Roboto:ital,wght@0,100;0,300;0,400;0,700;1,400&display=swap">
<style>
  :root {
    --brand-red: #e41e26;
    --slate: #3c3f3d;
    --ink: #1a1a1a;
    --paper: #ffffff;
    --cloud-light: #d9d9d9;
    --cloud-dark: #2b2b2b;
    --cloud-red: #8e1b1b;
  }
  * { margin: 0; padding: 0; box-sizing: border-box; }
  html, body { width: 1200px; height: 755px; overflow: hidden; background: var(--paper); }
  body { font-family: "Roboto", Arial, sans-serif; color: var(--ink); }

  .ad { position: relative; width: 1200px; height: 755px; background: var(--paper); overflow: hidden; }

  .brand-panel {
    position: absolute; left: 0; top: 0; width: 638px; height: 600px;
    background: var(--brand-red); color: var(--paper);
  }
  .licence {
    position: absolute; left: 28px; top: 10px;
    font-size: 15px; font-style: italic; font-weight: 400;
  }
  .company-name {
    position: absolute; left: 28px; top: 56px;
    font-size: 41px; font-weight: 700; letter-spacing: -0.3px; white-space: nowrap;
  }
  .tagline-band {
    position: absolute; left: 0; top: 125px; width: 638px; height: 146px;
    background: var(--slate); color: var(--paper);
  }
  .tagline-word {
    position: absolute; left: 20px; top: -2px;
    font-size: 136px; font-weight: 100; line-height: 1; letter-spacing: -3px;
  }
  .tagline-divider {
    position: absolute; left: 337px; top: 14px; width: 2px; height: 118px; background: var(--paper);
  }
  .tagline-list {
    position: absolute; left: 354px; top: 12px; list-style: none;
    font-size: 44px; font-weight: 300; line-height: 41px; white-space: nowrap;
  }
  .services-intro {
    position: absolute; left: 34px; top: 284px;
    font-size: 28px; font-weight: 700; line-height: 35px;
  }
  .services-list {
    position: absolute; left: 34px; top: 362px; list-style: none;
    font-size: 25px; font-weight: 400; white-space: nowrap;
  }
  .services-list li { height: 37px; line-height: 37px; padding-left: 32px; position: relative; }
  .services-list li::before {
    content: ""; position: absolute; left: 2px; top: 17px; width: 5px; height: 5px;
    border-radius: 50%; background: var(--paper);
  }

  .word-cloud {
    position: absolute; left: 688px; top: 8px; width: 470px; height: 572px;
    border-radius: 46% 46% 30% 38% / 40% 40% 22% 30%;
    background: radial-gradient(ellipse at 45% 40%, var(--cloud-light) 0%, #9a9a9a 45%, var(--cloud-red) 80%, var(--cloud-dark) 100%);
  }

  .contact { position: absolute; font-size: 22px; color: var(--ink); }
  .address { left: 94px; top: 620px; line-height: 26px; }
  .icon { position: absolute; }
  .contact-row { position: absolute; top: 692px; left: 0; width: 1200px; height: 36px; }
  .contact-item { position: absolute; top: 0; display: flex; align-items: center; gap: 4px; font-size: 25px; white-space: nowrap; }
  .footer-rule { position: absolute; left: 0; top: 743px; width: 1200px; height: 12px; background: var(--slate); }
</style>
</head>
<body>
<main class="ad">
  <section class="brand-panel">
    <p class="licence">Australian Credit Licence 512 604</p>
    <h1 class="company-name">Ridgeway Accounting &amp; Finance</h1>
    <div class="tagline-band">
      <span class="tagline-word">Local</span>
      <span class="tagline-divider"></span>
      <ul class="tagline-list">
        <li>Knowledge</li>
        <li>Beyond</li>
        <li>Compare</li>
      </ul>
    </div>
    <p class="services-intro">We are here for you all year round to<br>assist with...</p>
    <ul class="services-list">
      <li>Accounting &amp; Taxation</li>
      <li>Business Advice</li>
      <li>GST &amp; BAS’s</li>
      <li>Self Managed Super Funds</li>
      <li>Mortgage Broking and Loan Structuring</li>
      <li>Bookkeeping</li>
    </ul>
  </section>

  <div class="word-cloud" role="img" aria-label="Head-shaped word cloud of finance terms such as taxes, accountant, banking, income and economy"></div>

  <svg class="icon" style="left:28px;top:620px" width="52" height="56" viewBox="0 0 52 56" aria-hidden="true">
    <path d="M4 20 Q4 6 18 6 H40 Q48 6 48 16 V34 H4 Z" fill="#111"/>
    <rect x="22" y="34" width="7" height="22" fill="#111"/>
    <rect x="36" y="2" width="3" height="16" fill="#111"/>
    <rect x="36" y="2" width="10" height="6" fill="#111"/>
  </svg>
  <p class="contact address">Shop 3 Harbour Arcade, 12 Kellan St. Port Waverly<br>PO Box 418 Port Waverly 6790</p>

  <div class="contact-row">
    <span class="contact-item" style="left:30px">
      <svg width="36" height="28" viewBox="0 0 36 28" aria-hidden="true">
        <path d="M2 10 Q18 -2 34 10 L30 14 L24 11 V8 Q18 6 12 8 V11 L6 14 Z" fill="#111"/>
        <path d="M8 14 H28 L32 26 H4 Z" fill="#111"/>
        <circle cx="18" cy="20" r="4" fill="#fff"/>
      </svg>9051 3384</span>
    <span class="contact-item" style="left:214px">
      <svg width="36" height="34" viewBox="0 0 36 34" aria-hidden="true">
        <rect x="1" y="8" width="8" height="25" fill="#111"/>
        <rect x="11" y="1" width="18" height="12" fill="#111"/>
        <rect x="11" y="14" width="24" height="19" fill="#111"/>
        <g fill="#fff"><rect x="15" y="18" width="4" height="3"/><rect x="22" y="18" width="4" height="3"/><rect x="15" y="24" width="4" height="3"/><rect x="22" y="24" width="4" height="3"/></g>
      </svg>9051 3385</span>
    <span class="contact-item" style="left:406px">
      <svg width="40" height="34" viewBox="0 0 40 34" aria-hidden="true">
        <path d="M2 14 L20 2 L38 14 V32 H2 Z" fill="#fff" stroke="#111" stroke-width="2.5"/>
        <path d="M2 14 L20 26 L38 14" fill="none" stroke="#111" stroke-width="2.5"/>
        <text x="20" y="19" font-size="11" text-anchor="middle" font-family="Roboto, Arial, sans-serif" fill="#111">@</text>
      </svg>reception@rwaf.com.au</span>
    <span class="contact-item" style="left:768px">
      <svg width="38" height="34" viewBox="0 0 38 34" aria-hidden="true">
        <ellipse cx="19" cy="17" rx="18" ry="16" fill="#111"/>
        <text x="19" y="21" font-size="11" font-weight="700" text-anchor="middle" font-family="Roboto, Arial, sans-serif" fill="#fff">www</text>
      </svg>www.rwaf.com.au</span>
  </div>

  <div class="footer-rule"></div>
</main>
</body>
</html>
```